Smoker Oven Manufacturer Looking for Commercial Product Catalog

We are a small, family owned/operated international smoker oven manufacturer known for our end products and customer service. Our products include residential smokers, residential pellet grills, competition barbecue smokers, commercial smokers, commercial charbroilers, grilling and smoker accessories, sauces, spices, woods and food grade pellets. We have 6 international distributors and ship products everywhere.
Up until now, we have used individual spec sheets and a customized folder to send out information to prospects and we would like to move over to a catalog design.
We would like the final design to include red and our logo. The inside of the catalog is not as important to us as the cover, but we would like something that flows well. We like using food pictures as attention grabbers but also need balance so people who see our catalog do not think we are a restaurant. The end catalog will be about 20 pages.
Attached you will find examples of our spec sheets and the order we would like products in plus some of our current smoker images. For more information, please see our website: www.brinvale.com.
All of the product spec, past branding and content layout can be found in dropbox: https://www.filorama.net/sh/qp4tzwalbnro83x/KKTR2p9hqzvaTT5n1-dmWqx7b?dl=0

Target Market(s)

Owners/Operators/Chefs in the food industry

Industry/Entity Type

Commercial

Contact Information for Business Card

similar look and feel to the catalog

Colors
ec1f27
000000

Requirements
Must have
• Brinvale Logo, Red in the design but does not have to be the primary color used, products photos
Nice to have
• Food pictures

```html
<!DOCTYPE html>
<html lang="en">
<head>
<meta charset="utf-8">
<title>Brinvale Product Catalog 2017-18 — Cover</title>
<link href="https://fonts.googleapis.com/css2?family=Open+Sans:wght@300;400;700&display=swap" rel="stylesheet">
<style>
  :root {
    --backdrop: #e9e6e1;
    --charcoal: #2b3134;
    --brand-red: #ec1f27;
    --deep-red: #c8161d;
    --steel-light: #eef0f1;
    --steel-mid: #c9cdd0;
    --text-light: #e8eaeb;
    --text-muted: #9aa1a5;
    --white: #ffffff;
  }
  * { box-sizing: border-box; margin: 0; padding: 0; }
  html, body {
    width: 1200px; height: 804px; overflow: hidden;
    background: var(--backdrop);
    font-family: "Open Sans", sans-serif;
  }
  .cover {
    position: absolute; left: 330px; top: 27px;
    width: 540px; height: 750px;
    background: var(--charcoal);
    box-shadow: 0 10px 30px rgba(0,0,0,0.25);
    overflow: hidden;
  }
  .intro {
    position: absolute; left: 38px; top: 110px; width: 200px;
    font-size: 11px; line-height: 1.45; font-weight: 400;
    color: var(--text-light); letter-spacing: 0.2px;
  }
  .intro .accent { color: var(--brand-red); }
  .product-photo {
    position: absolute;
    background: radial-gradient(ellipse at 50% 55%, var(--white) 0%, var(--steel-light) 45%, var(--steel-mid) 100%);
  }
  .product-photo--top { left: 250px; top: 0; width: 290px; height: 250px; }
  .product-photo--bottom { left: 300px; top: 480px; width: 240px; height: 270px; }
  .food-photo {
    position: absolute; left: 0; top: 250px; width: 300px; height: 270px;
    background: radial-gradient(ellipse at 55% 45%, #c8702c 0%, #8e3f17 45%, #2a1a12 100%);
  }
  .title-panel {
    position: absolute; left: 300px; top: 250px; width: 240px; height: 230px;
    background: linear-gradient(135deg, var(--brand-red), var(--deep-red));
    color: var(--white);
    display: flex; flex-direction: column; justify-content: center;
    padding-left: 50px;
  }
  .title-panel h1 {
    font-size: 25px; font-weight: 700; line-height: 1.3; letter-spacing: 0.3px;
  }
  .title-panel .edition {
    font-size: 28px; font-weight: 300; margin-top: 6px; letter-spacing: 0.5px;
  }
  .brand {
    position: absolute; left: 50px; top: 598px;
    display: flex; align-items: center; gap: 10px;
  }
  .brand-mark { width: 14px; height: 14px; background: var(--brand-red); }
  .brand-name {
    font-size: 30px; font-weight: 700; color: var(--white); letter-spacing: 1px;
  }
  .website {
    position: absolute; left: 70px; top: 706px;
    font-size: 10px; letter-spacing: 3px; color: var(--text-muted);
  }
</style>
</head>
<body>
  <main class="cover">
    <p class="intro">Brinvale is the leading authority in <span class="accent">barbecue cooking products and technology</span>. We provide high-end products with exceptional satisfaction to our customers.</p>

    <div class="product-photo product-photo--top" role="img" aria-label="Stainless steel commercial rotisserie smoker with open door"></div>

    <div class="food-photo" role="img" aria-label="Golden roasted chickens on a grill rack"></div>

    <section class="title-panel">
      <h1>PRODUCT<br>CATALOG</h1>
      <p class="edition">2017-18</p>
    </section>

    <div class="product-photo product-photo--bottom" role="img" aria-label="Large stainless steel commercial smoker cabinet on casters"></div>

    <div class="brand">
      <span class="brand-name">BRINVALE</span>
      <span class="brand-mark"></span>
    </div>

    <p class="website">www.brinvale.com</p>
  </main>
</body>
</html>
```